Tolvik's Trim spring flyers

I am needing a flyer design for my lawn mowing business. my services are mowing, edging, weed eating, vacuuming with strong attention to detail. residential and commercial. Mowing average $35 and Spring clean up average $79. Looking for fun, professional and colorful to grab the eye and stand out. rough sizing of 10"x4"

Target Market(s)

people needing lawn care and spring clean up

Font styles to use
Serif

Colors

Designer to choose colors to be used in the design.

Requirements
Must have
• Services listed and pricing listed
• please add licensed and insured
• 417-555-0183
• dorsebrian7@fernmail.test
• FREE ESTIMATES

```html
<!DOCTYPE html>
<html lang="en">
<head>
<meta charset="utf-8">
<title>Tolvik's Trim Spring Flyer</title>
<link href="https://fonts.googleapis.com/css2?family=Montserrat:wght@500;600;700;800&display=swap" rel="stylesheet">
<style>
  :root {
    --blue: #1f72c4;
    --green: #2fae3b;
    --green-dark: #22922d;
    --navy: #123a5e;
    --ink: #2d2d2d;
    --white: #ffffff;
    --silver: #c9cdd1;
    --silver-dark: #8d9297;
    --seal-ink: #4a4f54;
    --photo-sky: #b9d2e6;
    --photo-stone: #c9bba3;
    --photo-lawn: #4f8f2c;
    --photo-lawn-deep: #3f7a22;
  }
  * { margin: 0; padding: 0; box-sizing: border-box; }
  html, body { width: 1200px; height: 3004px; overflow: hidden; background: var(--white); }
  .flyer {
    position: relative; width: 1200px; height: 3004px; overflow: hidden;
    background: var(--white);
    font-family: "Montserrat", Arial, sans-serif;
  }
  .backdrop { position: absolute; inset: 0; }
  .brand {
    position: absolute; top: 130px; left: 470px; width: 640px;
    text-align: center;
  }
  .brand-mark {
    display: inline-block; width: 110px; height: 110px; border-radius: 50%;
    background: var(--navy); margin-bottom: 24px;
  }
  .brand-name {
    font-weight: 800; font-size: 74px; color: var(--navy);
    letter-spacing: 2px; line-height: 1; text-transform: uppercase;
  }
  .seal {
    position: absolute; left: 700px; top: 560px; width: 320px; height: 320px;
  }
  .services {
    position: absolute; right: 150px; top: 1615px;
    list-style: none; text-align: right;
    color: var(--white); font-weight: 700; font-size: 86px;
    line-height: 126px; letter-spacing: 1px;
  }
  .price-card {
    position: absolute; top: 2200px; width: 240px; height: 350px;
    background: var(--green); border: 8px solid var(--white); border-radius: 34px;
    color: var(--white); text-align: center; font-weight: 700;
  }
  .price-card.reach { left: 172px; }
  .price-card.mowing { left: 500px; }
  .price-card.cleanup { left: 820px; }
  .price-card .tab {
    position: absolute; left: 50%; top: -8px; transform: translateX(-50%);
    width: 140px; height: 110px; border-radius: 0 0 70px 70px;
    border: 8px solid var(--white); border-top: none; background: var(--green);
  }
  .price-card .icon { width: 130px; height: 130px; margin: 26px auto 0; display: block; }
  .price-card .label { font-size: 48px; line-height: 56px; }
  .price-card.reach .label {
    position: absolute; left: 0; right: 0; top: 150px;
    font-size: 30px; line-height: 44px;
  }
  .contact {
    position: absolute; right: 140px; top: 2620px; text-align: right;
    color: var(--ink); font-weight: 600; font-size: 50px; line-height: 92px;
  }
  .cta {
    position: absolute; left: 0; right: 0; top: 2815px; text-align: center;
    color: var(--green); font-weight: 700; font-size: 86px; letter-spacing: 2px;
  }
</style>
</head>
<body>
<div class="flyer">
  <svg class="backdrop" width="1200" height="3004" viewBox="0 0 1200 3004">
    <defs>
      <linearGradient id="houseTones" x1="0" y1="0" x2="0" y2="1">
        <stop offset="0" stop-color="var(--photo-sky)"/>
        <stop offset="0.45" stop-color="var(--photo-stone)"/>
        <stop offset="0.75" stop-color="var(--photo-lawn)"/>
        <stop offset="1" stop-color="var(--photo-lawn-deep)"/>
      </linearGradient>
    </defs>
    <polygon points="0,180 220,180 0,330" fill="var(--blue)"/>
    <polygon points="0,1160 1200,1160 1200,2480 0,2160" fill="var(--blue)"/>
    <polygon role="img" aria-label="Photo of a stone-front family home with a trimmed green lawn and shrubs"
      points="0,340 1200,1000 1200,1160 0,2180" fill="url(#houseTones)"/>
    <polygon points="0,2180 1200,1160 1200,1205 0,2225" fill="var(--green)"/>
  </svg>

  <header class="brand">
    <span class="brand-mark"></span>
    <div class="brand-name">Tolvik's Trim</div>
  </header>

  <svg class="seal" viewBox="0 0 320 320" role="img" aria-label="Licensed and insured seal">
    <circle cx="160" cy="160" r="156" fill="var(--silver-dark)"/>
    <circle cx="160" cy="160" r="140" fill="var(--silver)" stroke="var(--white)" stroke-width="6"/>
    <g transform="rotate(-18 160 160)" text-anchor="middle" font-family="Montserrat, Arial, sans-serif" font-weight="800" fill="var(--seal-ink)">
      <text x="160" y="100" font-size="22">★★★</text>
      <text x="160" y="154" font-size="40">LICENSED</text>
      <text x="160" y="202" font-size="34">&amp; INSURED</text>
      <text x="160" y="240" font-size="22">★★★</text>
    </g>
  </svg>

  <ul class="services">
    <li>MOWING</li>
    <li>EDGING</li>
    <li>WEED EATING</li>
    <li>VACUUMING</li>
  </ul>

  <div class="price-card reach">
    <span class="tab"></span>
    <div class="label">Residential<br>&amp;<br>Commercial</div>
  </div>

  <div class="price-card mowing">
    <svg class="icon" viewBox="0 0 130 130" aria-hidden="true">
      <circle cx="65" cy="65" r="60" fill="var(--white)"/>
      <path d="M28 42 L48 66 H96 V88 H34 V66" fill="none" stroke="var(--green-dark)" stroke-width="7" stroke-linejoin="round"/>
      <rect x="48" y="66" width="48" height="22" fill="var(--green-dark)"/>
      <circle cx="44" cy="94" r="9" fill="var(--green-dark)"/>
      <circle cx="88" cy="94" r="9" fill="var(--green-dark)"/>
    </svg>
    <div class="label">Mowing<br>$35</div>
  </div>

  <div class="price-card cleanup">
    <svg class="icon" viewBox="0 0 130 130" aria-hidden="true">
      <circle cx="65" cy="65" r="60" fill="var(--white)"/>
      <line x1="90" y1="24" x2="62" y2="72" stroke="var(--green-dark)" stroke-width="7" stroke-linecap="round"/>
      <path d="M50 66 L76 80 L64 104 L32 92 Z" fill="var(--green-dark)"/>
    </svg>
    <div class="label">Spring<br>clean up<br>$79</div>
  </div>

  <div class="contact">
    <div class="phone">417-555-0183</div>
    <div class="email">dorsebrian7@fernmail.test</div>
  </div>

  <div class="cta">FREE ESTIMATES</div>
</div>
</body>
</html>
```